Portrait of a Learner Infographic

A portrait of a learner is an aspirational idea of the skills a student should have at graduation. "Learner" recognizes that learning continues after graduation.
An info graphic is needed to convey the skills that have been identified. A full version is needed that can be posted on classroom walls (11x17) and a simplified version to share on the website and any other means identified.
The Birchfield School District is in Concord, New Hampshire, the capital city for NH. The district serves 4,100 diverse students in seven schools and a regional career and technical education center.
The district's hex colors are Green: #007137 and Blue: #085bab
Each school has its own unique colors.
The design should be positive, aspirational and still professional.
Teachers, students and parents
Public school district

```html
<!DOCTYPE html>
<html lang="en">
<head>
<meta charset="utf-8">
<title>Portrait of a Learner</title>
<link href="https://fonts.googleapis.com/css2?family=Russo+One&family=Exo+2:wght@400;500&display=swap" rel="stylesheet">
<style>
  :root{
    --green:#0f6e3b;
    --brick:#6e3532;
    --brick-dark:#431b18;
    --frame-grey:#f2f2f3;
    --pill-line:#dcdcde;
    --ink:#1d1d1b;
    --panel:#e6e7e8;
    --teal:#1aa9b6;
    --paper:#ffffff;
  }
  *{margin:0;padding:0;box-sizing:border-box}
  html,body{width:1200px;height:1200px;overflow:hidden;background:var(--paper)}
  body{position:relative;font-family:"Exo 2",sans-serif;color:var(--ink)}
  .poster-mat{position:absolute;left:272px;top:81px;width:624px;height:1039px;background:var(--frame-grey)}
  .brick-frame{position:absolute;left:291px;top:89px;width:595px;height:1026px;background:var(--brick)}
  .pillar{position:absolute;top:240px;width:39px;height:710px;background:var(--brick-dark)}
  .pillar.left{left:291px}
  .pillar.right{left:847px}
  .sheet{position:absolute;left:330px;top:243px;width:517px;height:833px;background:var(--paper)}
  .sheet-top{position:absolute;left:351px;top:129px;width:474px;height:120px;background:var(--paper)}
  .title{position:absolute;left:330px;top:160px;width:517px;text-align:center;font-family:"Russo One",sans-serif;color:var(--green);font-size:49px;line-height:54px;letter-spacing:1px}
  .mission{position:absolute;left:360px;top:300px;width:457px;text-align:center;color:var(--green);font-size:9.6px;line-height:11.5px}
  .trait{position:absolute;width:134px;height:52px;border:1px solid var(--pill-line);border-radius:26px;display:flex;align-items:center;gap:9px;padding:0 8px;font-size:9.8px;line-height:10.5px}
  .trait.num-right{flex-direction:row-reverse;justify-content:flex-start;text-align:right}
  .badge{flex:none;width:31px;height:31px;border-radius:50%;background:var(--green);color:#fff;font-family:"Russo One",sans-serif;font-size:8.6px;display:flex;align-items:center;justify-content:center}
  .trait-label{flex:1}
  .trait.num-right .trait-label{flex:none}
  .pillar-tag{position:absolute;height:32px;background:var(--green);color:#fff;border-radius:3px;font-family:"Russo One",sans-serif;font-size:9px;letter-spacing:.3px;display:flex;align-items:center;justify-content:center}
  .connectors{position:absolute;left:0;top:0}
  .graduate{position:absolute;left:501px;top:612px;width:173px;height:188px;background:linear-gradient(180deg,#f1f1f3 0%,#e9eaec 40%,var(--teal) 78%,#148c97 100%);border-radius:86px 86px 4px 4px}
  .podium{position:absolute;left:498px;top:795px;width:173px;height:5px;background:#111}
  .pillar-table{position:absolute;left:372px;top:838px;width:430px;display:grid;grid-template-columns:142px 142px 142px;column-gap:2px}
  .col-head{height:26px;background:var(--green);color:#fff;font-family:"Russo One",sans-serif;font-size:8.4px;display:flex;align-items:center;justify-content:center}
  .col-body{margin-top:5px;height:168px;background:var(--panel);padding:15px 10px 0 14px;font-size:6.4px;line-height:8.4px}
  .col-body p{margin-bottom:8.4px}
  .col-body.tight p{margin-bottom:0}
</style>
</head>
<body>
  <div class="poster-mat"></div>
  <div class="brick-frame" role="img" aria-label="Red brick wall frame"></div>
  <div class="pillar left"></div>
  <div class="pillar right"></div>
  <div class="sheet-top"></div>
  <div class="sheet"></div>

  <h1 class="title">PORTRAIT OF A<br>LEARNER</h1>
  <p class="mission">Birchfield School District learners are informed, compassionate and capable citizens who effectively, courageously and responsibly direct their lives and positively impact communities</p>

  <svg class="connectors" width="1200" height="1200" viewBox="0 0 1200 1200">
    <g fill="none" stroke="#d5d5d8" stroke-width="1">
      <path d="M568 524 q20 0 20 14 V557"/>
      <path d="M504 652 q-67 0 -67 26 V707"/>
      <path d="M801 628 q-67 0 -67 26 V707"/>
      <path d="M588 589 V612"/>
      <path d="M501 723 H527 M674 723 H676"/>
    </g>
    <g fill="var(--green)" stroke="#fff" stroke-width="2.5">
      <circle cx="588" cy="557" r="5"/>
      <circle cx="437" cy="707" r="5"/>
      <circle cx="734" cy="707" r="5"/>
    </g>
  </svg>

  <!-- Creative & Skillful column -->
  <div class="trait" style="left:371px;top:368px"><span class="badge">06</span><span class="trait-label">Critical and analyti-<br>cal thinker</span></div>
  <div class="trait num-right" style="left:371px;top:420px"><span class="badge">05</span><span class="trait-label">Innovative</span></div>
  <div class="trait" style="left:371px;top:472px"><span class="badge">04</span><span class="trait-label">Informed risk-taker</span></div>
  <div class="trait num-right" style="left:371px;top:524px"><span class="badge">03</span><span class="trait-label">Adaptable</span></div>
  <div class="trait" style="left:371px;top:576px"><span class="badge">02</span><span class="trait-label">Curious</span></div>
  <div class="trait num-right" style="left:371px;top:628px"><span class="badge">01</span><span class="trait-label">Self-motivated</span></div>

  <!-- Collaborative column -->
  <div class="trait" style="left:518px;top:368px"><span class="badge">03</span><span class="trait-label">Compassionate<br>leader</span></div>
  <div class="trait num-right" style="left:518px;top:420px"><span class="badge">02</span><span class="trait-label">Civic minded</span></div>
  <div class="trait" style="left:518px;top:472px;width:150px"><span class="badge">01</span><span class="trait-label">Emotional intelligence</span></div>

  <!-- Self-directed column -->
  <div class="trait num-right" style="left:667px;top:368px"><span class="badge">05</span><span class="trait-label">Growth mindset</span></div>
  <div class="trait" style="left:667px;top:420px"><span class="badge">04</span><span class="trait-label">Resilient</span></div>
  <div class="trait num-right" style="left:667px;top:472px"><span class="badge">03</span><span class="trait-label">Self-starter</span></div>
  <div class="trait" style="left:667px;top:524px"><span class="badge">02</span><span class="trait-label">Problem solver</span></div>
  <div class="trait num-right" style="left:667px;top:576px"><span class="badge">01</span><span class="trait-label">Responsible</span></div>

  <div class="pillar-tag" style="left:530px;top:557px;width:114px">COLLABORATIVE</div>
  <div class="pillar-tag" style="left:371px;top:707px;width:130px">CREATIVE &amp; SKILLFUL</div>
  <div class="pillar-tag" style="left:676px;top:707px;width:125px">SELF-DIRECTED</div>

  <div class="graduate" role="img" aria-label="Illustration of a graduate in cap and teal gown"></div>
  <div class="podium"></div>

  <div class="pillar-table">
    <div class="col-head">COLLABORATIVE</div>
    <div class="col-head">SELF-DIRECTED</div>
    <div class="col-head">CREATIVE &amp; SKILLFUL</div>
    <div class="col-body">
      <p>Respectfully engages with others</p>
      <p>Asks challenging and probing questions in a manner that preserves healthy relationships</p>
      <p>Speaks and acts inclusively to support equity, safety and belonging with actions and behaviors that support an environment where all feel safe to learn and engage</p>
      <p>Demonstrates and advocates for positive and sustainable change for oneself and others</p>
    </div>
    <div class="col-body tight">
      <p>Understands own strengths, needs and interests</p>
      <p>Accesses credible resources and seeks help to support growth and create actionable plans</p>
      <p>Uses effective time management, planning and communication to accomplish long and short-term goals</p>
      <p>Perseveres through challenges and seeking new experiences</p>
      <p>Approaches problems as opportunities and generates solutions</p>
    </div>
    <div class="col-body tight">
      <p>Accesses, evaluates, applies and communicates diverse forms of information for a variety of audiences and purposes</p>
      <p>Makes productive and innovative decisions based on new learning that move an idea from concept to application</p>
      <p>Gains awareness of relevant technology and practices that enable production in a variety of fields</p>
      <p>Learns processes that enable individuals and collaborative teams to plan, design, test, execute, evaluate, reflect and adapt</p>
      <p>Uses evidence of successes and challenges to adapt practices</p>
    </div>
  </div>
</body>
</html>
```